Torvel, Inc. new buisness cards - brand guide included

We need new business cards. SLEAK SIMPLE FINANCE. They must include a place for NAME, TITLE, CELL, OFFICE PHONE, EMAIL. they also must include our services across the bottom. AIR, OCEAN, FTL, LTL, EXPRESS. for reference this will be being handed to some of the most prestigious shipping companies in a america.

Target Market(s)

Finance and corporate

Contact Information for Business Card

We need new business cards. SLEAK SIMPLE FINANCE. They must include a place for NAME, TITLE, CELL, OFFICE PHONE, EMAIL. they also must include our services across the bottom. AIR, OCEAN, FTL, LTL, EXPRESS.

Requirements
Must have
• We need new business cards. SLEAK SIMPLE FINANCE. They must include a place for NAME, TITLE, CELL, OFFICE PHONE, EMAIL. they also must include our services across the bottom. AIR, OCEAN, FTL, LTL, EXPRESS.
Nice to have
• USE THE COLORS AND LOGO IN THE BRAND GUIDE :)

```html
<!DOCTYPE html>
<html lang="en">
<head>
<meta charset="utf-8">
<title>Torvel, Inc. Business Cards</title>
<link href="https://fonts.googleapis.com/css2?family=EB+Garamond:wght@400;500&display=swap" rel="stylesheet">
<style>
  :root {
    --page: #e6e4e2;
    --ink: #1c1c1c;
    --card-dark: #1f1f1f;
    --card-light: #f4f4f3;
    --gold: #b3a68a;
    --gold-text: #a6967a;
    --cream: #ece6da;
  }
  * { box-sizing: border-box; margin: 0; padding: 0; }
  html, body { width: 1200px; height: 900px; overflow: hidden; }
  body {
    background: var(--page);
    font-family: "EB Garamond", Georgia, serif;
    color: var(--ink);
    position: relative;
  }
  .card {
    position: absolute;
    left: 320px;
    width: 560px;
    height: 320px;
    box-shadow: 0 10px 30px rgba(0,0,0,0.18);
    overflow: hidden;
  }
  .card--back { top: 100px; background: var(--card-dark); }
  .card--front { top: 480px; background: var(--card-light); }

  .back-texture {
    position: absolute; inset: 0;
    background: linear-gradient(135deg, #232323, #1a1a1a);
  }
  .back-name {
    position: absolute; inset: 0;
    display: flex; align-items: center; justify-content: center;
    font-size: 54px; font-weight: 400; letter-spacing: 8px;
    color: var(--cream);
  }

  .front-name {
    position: absolute; left: 52px; top: 118px;
    font-size: 40px; font-weight: 400; letter-spacing: 5px;
    color: var(--ink);
  }
  .contact {
    position: absolute; left: 318px; top: 40px;
  }
  .contact__name {
    font-size: 22px; letter-spacing: 2px; text-transform: uppercase;
    color: var(--gold-text); line-height: 1;
  }
  .contact__title {
    font-size: 9px; letter-spacing: 2.6px; text-transform: uppercase;
    color: #555; margin-top: 4px;
  }
  .contact__list { list-style: none; margin-top: 22px; }
  .contact__item {
    display: flex; align-items: center; gap: 10px;
    font-size: 17px; line-height: 26px; color: var(--ink);
  }
  .contact__icon { width: 14px; height: 14px; flex: none; }
  .services {
    position: absolute; left: 0; right: 0; top: 236px; height: 40px;
    background: var(--gold);
    display: flex; align-items: center; justify-content: center; gap: 14px;
    font-size: 19px; letter-spacing: 2.5px; color: #fff;
  }
  .services__sep { opacity: 0.8; }
</style>
</head>
<body>
  <section class="card card--back">
    <div class="back-texture" role="img" aria-label="Dark card face with a subtle tone-on-tone repeating pattern"></div>
    <div class="back-name">TORVEL</div>
  </section>

  <section class="card card--front">
    <div class="front-name">TORVEL</div>
    <div class="contact">
      <p class="contact__name">Daniel Hart</p>
      <p class="contact__title">Accounting Manager</p>
      <ul class="contact__list">
        <li class="contact__item">
          <svg class="contact__icon" viewBox="0 0 14 14"><rect x="3.5" y="1" width="7" height="12" rx="1.2" fill="none" stroke="#8a7f6a" stroke-width="1.2"/><circle cx="7" cy="11" r="0.7" fill="#8a7f6a"/></svg>
          555-0142-2288
        </li>
        <li class="contact__item">
          <svg class="contact__icon" viewBox="0 0 14 14"><path d="M3 1.5 L5.5 1.5 L6.3 4.3 L4.8 5.5 Q6 8.2 8.5 9.3 L9.7 7.8 L12.5 8.6 L12.5 11 Q12.5 12.5 11 12.5 Q2 11.5 1.5 3 Q1.5 1.5 3 1.5 Z" fill="#8a7f6a"/></svg>
          555-010-4417
        </li>
        <li class="contact__item">
          <svg class="contact__icon" viewBox="0 0 14 14"><rect x="1" y="3" width="12" height="8.5" fill="#8a7f6a"/><path d="M1 3 L7 8 L13 3" fill="none" stroke="#f4f4f3" stroke-width="1"/></svg>
          dhart@torvelinc.com
        </li>
      </ul>
    </div>
    <div class="services">
      <span>AIR</span><span class="services__sep">|</span>
      <span>OCEAN</span><span class="services__sep">|</span>
      <span>FTL</span><span class="services__sep">|</span>
      <span>LTL</span><span class="services__sep">|</span>
      <span>EXPRESS.</span>
    </div>
  </section>
</body>
</html>
```